Shop Front Design

We are Corvel Welding Supplies, a welding products suppliers just north of London.
We would like a banner 4.0m x 1.5m that will be placed above our building entrance to introduce our business to regular and new customers. Info we would like lister:
-Our Logo (CWS logo1)
-Core info: email address, phone number, opening hours
cwsarc@mailfern.net
07412 558 190
Monday to Friday 12:00 - 18:00
Saturday 09:00 - 12:00
-Our core services:
Welders & Consumables
Hire
Industrial Gases
Training Courses
-Our core suppliers logos. I would like to see what impact they would have on the banner
Preferred colour theme orange and grey.

```html
<!DOCTYPE html>
<html lang="en">
<head>
<meta charset="utf-8">
<title>Corvel Welding Supplies – Shop Front Banner</title>
<link href="https://fonts.googleapis.com/css2?family=Exo+2:ital,wght@1,900&family=Poppins:wght@400;600&display=swap" rel="stylesheet">
<style>
  :root {
    --backdrop: #e5eaea;
    --white: #ffffff;
    --panel-grey: #e9eeed;
    --brand-grey: #5a6566;
    --signal-red: #fa3a0e;
    --amber: #fb7d0c;
    --ink: #151515;
    --text-dark: #1a1a1a;
  }
  * { margin: 0; padding: 0; box-sizing: border-box; }
  html, body { width: 1200px; height: 1200px; overflow: hidden; background: var(--backdrop); }
  .banner {
    position: absolute; left: 90px; top: 400px;
    width: 1024px; height: 383px;
    background: var(--white);
    overflow: hidden;
    font-family: "Poppins", sans-serif;
  }
  .banner-shapes { position: absolute; inset: 0; }
  .brand {
    position: absolute; left: 34px; top: 62px; width: 360px;
    display: flex; align-items: center; gap: 14px;
  }
  .brand-dot { width: 46px; height: 46px; border-radius: 50%; background: var(--amber); flex: none; }
  .brand-name {
    font-family: "Poppins", sans-serif; font-weight: 600;
    font-size: 27px; line-height: 1.1; color: var(--brand-grey);
  }
  .hours { position: absolute; left: 34px; color: var(--text-dark); }
  .hours-day { font-size: 27px; font-weight: 400; line-height: 1; }
  .hours-time { font-size: 27px; font-weight: 600; line-height: 1; color: var(--signal-red); margin-top: 6px; }
  .hours.weekdays { top: 222px; }
  .hours.saturday { top: 303px; }
  .service {
    position: absolute; transform: translateX(-50%);
    text-align: center; white-space: nowrap;
    font-family: "Exo 2", sans-serif; font-style: italic; font-weight: 900;
    font-size: 30px; line-height: 32px; color: var(--white);
    letter-spacing: 0.2px;
  }
  .service.welders { left: 568px; top: 102px; }
  .service.gases { left: 890px; top: 102px; }
  .service.hire { left: 568px; top: 251px; }
  .service.training { left: 890px; top: 251px; }
  .contact {
    position: absolute; top: 332px; height: 42px;
    display: flex; align-items: center;
    color: var(--white); font-size: 22px;
  }
  .contact.phone { left: 414px; letter-spacing: 0.5px; }
  .contact.email { left: 694px; letter-spacing: 2px; }
</style>
</head>
<body>
<div class="banner">
  <svg class="banner-shapes" width="1024" height="383" viewBox="0 0 1024 383">
    <rect class="hours-panel" x="0" y="193" width="400" height="190" fill="var(--panel-grey)"/>
    <polygon class="orange-stripe" points="381,193 392,193 311,383 300,383" fill="var(--amber)"/>
    <polygon class="services-field" points="460,0 1024,0 1024,383 320,383" fill="var(--signal-red)"/>
    <line class="service-divider" x1="742" y1="43" x2="742" y2="283" stroke="#ffffff" stroke-opacity="0.7" stroke-width="1.2" stroke-dasharray="4 6"/>

    <!-- service icons -->
    <g class="icon flask" transform="translate(568,63)">
      <circle r="33" fill="var(--amber)"/>
      <path d="M-5,-20 h10 M-4,-20 v14 l-12,22 h32 l-12,-22 v-14" fill="none" stroke="var(--ink)" stroke-width="2.4" stroke-linejoin="round"/>
      <line x1="-11" y1="8" x2="11" y2="8" stroke="var(--ink)" stroke-width="2"/>
    </g>
    <g class="icon factory" transform="translate(890,63)">
      <circle r="33" fill="var(--amber)"/>
      <path d="M-19,17 v-22 l10,-6 v6 l10,-6 v6 l10,-6 v-8 h8 v36 z" fill="none" stroke="var(--ink)" stroke-width="2.4" stroke-linejoin="round"/>
      <path d="M-9,12 v-6 M-3,12 v-6 M3,12 v-6 M9,12 v-6" stroke="var(--ink)" stroke-width="2"/>
    </g>
    <g class="icon network" transform="translate(568,214)">
      <circle r="33" fill="var(--amber)"/>
      <circle r="10" fill="none" stroke="var(--ink)" stroke-width="2.2"/>
      <circle cy="-3" r="3" fill="var(--ink)"/>
      <path d="M-5,6 q5,-7 10,0" fill="none" stroke="var(--ink)" stroke-width="2"/>
      <g stroke="var(--ink)" stroke-width="2" fill="none">
        <line x1="0" y1="-10" x2="0" y2="-18"/><circle cy="-21" r="3"/>
        <line x1="0" y1="10" x2="0" y2="18"/><circle cy="21" r="3"/>
        <line x1="-10" y1="0" x2="-18" y2="0"/><circle cx="-21" r="3"/>
        <line x1="10" y1="0" x2="18" y2="0"/><circle cx="21" r="3"/>
        <line x1="7" y1="-7" x2="12" y2="-12"/><circle cx="14.5" cy="-14.5" r="3"/>
        <line x1="-7" y1="-7" x2="-12" y2="-12"/><circle cx="-14.5" cy="-14.5" r="3"/>
        <line x1="7" y1="7" x2="12" y2="12"/><circle cx="14.5" cy="14.5" r="3"/>
        <line x1="-7" y1="7" x2="-12" y2="12"/><circle cx="-14.5" cy="14.5" r="3"/>
      </g>
    </g>
    <g class="icon training" transform="translate(890,214)">
      <circle r="33" fill="var(--amber)"/>
      <rect x="-8" y="-18" width="26" height="30" fill="none" stroke="var(--ink)" stroke-width="2"/>
      <path d="M-3,8 v-5 M3,8 v-9 M9,8 v-7 M14,8 v-13" stroke="var(--ink)" stroke-width="2"/>
      <circle cx="-15" cy="-12" r="3.5" fill="none" stroke="var(--ink)" stroke-width="2"/>
      <path d="M-19,18 v-20 h8 l6,-4 M-15,4 v14" fill="none" stroke="var(--ink)" stroke-width="2" stroke-linejoin="round"/>
    </g>

    <!-- contact strip -->
    <polygon class="email-strip" points="630,332 1024,332 1024,374 618,374" fill="var(--amber)"/>
    <polygon class="phone-strip" points="363,332 632,332 615,374 348,374" fill="var(--ink)"/>
    <path class="phone-icon" d="M376,344 q-3,3 0,9 q4,8 11,11 q5,2 7,-1 l-4,-4 l-3,2 q-5,-3 -7,-8 l2,-3 z" fill="none" stroke="var(--signal-red)" stroke-width="1.6" stroke-linejoin="round"/>
    <path class="phone-waves" d="M388,343 q5,1 6,6 M389,339 q8,2 10,10" fill="none" stroke="var(--signal-red)" stroke-width="1.4"/>
    <g class="mail-icon" fill="none" stroke="var(--ink)" stroke-width="1.8">
      <rect x="660" y="347" width="20" height="13"/>
      <path d="M660,347 l10,8 l10,-8 M660,360 l7,-6 M680,360 l-7,-6"/>
    </g>
  </svg>

  <div class="brand">
    <span class="brand-dot"></span>
    <span class="brand-name">Corvel Welding Supplies</span>
  </div>

  <div class="hours weekdays">
    <p class="hours-day">Monday to Friday</p>
    <p class="hours-time">12:00 - 18:00</p>
  </div>
  <div class="hours saturday">
    <p class="hours-day">Saturday</p>
    <p class="hours-time">09:00 - 12:00</p>
  </div>

  <div class="service welders">WELDERS &amp;<br>CONSUMABLES</div>
  <div class="service gases">INDUSTRIAL<br>GASES</div>
  <div class="service hire">HIRE</div>
  <div class="service training">TRAINING<br>COURSES</div>

  <div class="contact phone">07412 558 190</div>
  <div class="contact email">cwsarc@mailfern.net</div>
</div>
</body>
</html>
```